Book cover for middle grade children's book

I need a book cover design for the first book in my middle grade series aimed at girls ages 9-12.

PLEASE SEE MY ATTACHED EXAMPLES.

Title: Lila Dorsey: Cousin Marla's Scheme

Design Brief:
Front: I want it to look like a composition book. The background should be a pink plaid design. There should be a white square in the center like a composition book. On top of the square in purple letters should be the name Lila. Underneath the square should be the name Dorsey. Lila Dorsey should be in a fun girly font that's readible on thumbnail. The sub title should go on the white square where a kid would write their name. It should say Cousin Marla's Scheme in a girl's pink handwriting. At the bottom underneath Dorsey should be my name: Rochelle Anne Vukovic

On the left side there should be a dark pink or purple (whichever looks best with the pattern) strip like composition books have.

Spine: Lila Dorsey: Cousin Marla's Scheme (Lila Dorsey #1) Vukovic

On the back: I'd like the back to be hot pink with white font.

Thirteen-year-old Lila Dorsey has a lot on her plate. Her biggest challenge is living with her Cousin Marla. As much as Lila tries to please her aunt,, they always seem to butt heads. Sometimes Lila feels as if Cousin Marla goes out of her way to make her life miserable.

Cousin Marla enrolls Lila in a social group called the Golden Tulips, a group that's supposed to teach young girls how to be proper ladies, however it turns out to be nothing more than a club for snobs. Lila wants out, but she's made a deal with Cousin Marla. Will Lila take a stand against the Golden Tulips or will their snobbery rub off on her?
IT'S VERY IMPORTANT THAT IT LOOKS LIKE A COMPOSITION BOOK SINCE THAT WILL BE THE BRAND FOR THE SERIES.

I need this cover to fit the mandates for ebook and printhollow. Place follow the correct measurements.

This book will be 160 pages on cream paper. 6x9

Target Market(s)

Girls ages 9 and up

Industry/Entity Type

Club

Requirements
Must have
• Readable professional looking font
Should not have
• A background pattern that too busy and clashes with the font

```html
<!DOCTYPE html>
<html lang="en">
<head>
<meta charset="utf-8">
<title>Lila Dorsey: Cousin Marla's Scheme — Cover</title>
<link href="https://fonts.googleapis.com/css2?family=Cherry+Swash:wght@400;700&family=Dancing+Script:wght@500&family=Great+Vibes&family=Open+Sans:wght@400&family=Tinos:ital@1&display=swap" rel="stylesheet">
<style>
  :root {
    --back-pink: #ef62a0;
    --spine-pink: #e57aa8;
    --binding-strip: #dc0f7e;
    --plaid-light: #f7b6d0;
    --plaid-mid: #f39cc0;
    --plaid-deep: #ec80ae;
    --label-white: #ffffff;
    --title-purple: #7d2d82;
    --subtitle-pink: #ea6aa0;
    --rule-grey: #9a9a9a;
    --text-white: #ffffff;
  }
  html, body {
    margin: 0;
    padding: 0;
    overflow: hidden;
    background: #ffffff;
  }
  .cover {
    position: relative;
    width: 1200px;
    height: 870px;
    overflow: hidden;
  }
  .back-cover {
    position: absolute;
    left: 0; top: 0;
    width: 580px; height: 870px;
    background: var(--back-pink);
  }
  .blurb {
    position: absolute;
    left: 90px; top: 340px;
    width: 402px;
    margin: 0;
    font-family: "Tinos", "Times New Roman", serif;
    font-style: italic;
    font-size: 12.6px;
    line-height: 19.2px;
    color: var(--text-white);
    text-align: justify;
  }
  .blurb p { margin: 0 0 19px; }
  .spine {
    position: absolute;
    left: 580px; top: 0;
    width: 40px; height: 870px;
    background: var(--spine-pink);
  }
  .spine-title {
    position: absolute;
    left: 10px; top: 240px;
    writing-mode: vertical-rl;
    font-family: "Open Sans", Arial, sans-serif;
    font-size: 15px;
    color: var(--text-white);
    white-space: nowrap;
    letter-spacing: 0.1px;
  }
  .binding-strip {
    position: absolute;
    left: 620px; top: 0;
    width: 50px; height: 870px;
    background: var(--binding-strip);
  }
  .front-cover {
    position: absolute;
    left: 670px; top: 0;
    width: 530px; height: 870px;
  }
  .plaid-field {
    position: absolute;
    inset: 0;
    background: linear-gradient(135deg, var(--plaid-light), var(--plaid-mid) 55%, var(--plaid-deep));
  }
  .series-name {
    position: absolute;
    margin: 0;
    font-family: "Cherry Swash", cursive;
    font-weight: 400;
    color: var(--title-purple);
    line-height: 1;
  }
  .series-name--first { left: 95px; top: 270px; font-size: 82px; }
  .series-name--last { left: 135px; top: 548px; font-size: 82px; }
  .name-label {
    position: absolute;
    left: 96px; top: 370px;
    width: 290px; height: 176px;
    background: var(--label-white);
  }
  .subtitle {
    position: absolute;
    left: 0; right: 0; top: 20px;
    margin: 0;
    text-align: center;
    font-family: "Dancing Script", cursive;
    font-weight: 500;
    font-size: 29px;
    color: var(--subtitle-pink);
  }
  .write-line {
    position: absolute;
    left: 20px; width: 248px;
    border-top: 1px dotted var(--rule-grey);
  }
  .write-line--one { top: 100px; }
  .write-line--two { top: 137px; }
  .author {
    position: absolute;
    left: 285px; top: 630px;
    margin: 0;
    font-family: "Great Vibes", cursive;
    font-size: 12px;
    color: var(--title-purple);
    white-space: nowrap;
  }
</style>
</head>
<body>
<main class="cover">
  <section class="back-cover">
    <div class="blurb">
      <p>Thirteen-year-old Lila Dorsey has a lot on her plate. Her biggest challenge is living with her Cousin Marla. As much as Lila tries to please her aunt,, they always seem to butt heads. Sometimes Lila feels as if Cousin Marla goes out of her way to make her life miserable.</p>
      <p>Cousin Marla enrolls Lila in a social group called the Golden Tulips, a group that's supposed to teach young girls how to be proper ladies, however it turns out to be nothing more than a club for snobs. Lila wants out, but she's made a deal with Cousin Marla. Will Lila take a stand against the Golden Tulips or will their snobbery rub off on her?</p>
    </div>
  </section>

  <section class="spine">
    <span class="spine-title">Lila Dorsey: Cousin Marla's Scheme (Lila Dorsey #1) Vukovic</span>
  </section>

  <div class="binding-strip"></div>

  <section class="front-cover">
    <div class="plaid-field" role="img" aria-label="Pink and white gingham plaid pattern with small pink flowers"></div>
    <h1 class="series-name series-name--first">Lila</h1>
    <div class="name-label">
      <h2 class="subtitle">Cousin Marla's Scheme</h2>
      <div class="write-line write-line--one"></div>
      <div class="write-line write-line--two"></div>
    </div>
    <h1 class="series-name series-name--last">Dorsey</h1>
    <p class="author">Rochelle Anne Vukovic</p>
  </section>
</main>
</body>
</html>
```